Brightwell Wiring Needs A Logo Design

We need a logo for my new company based out of Sacramento, Ca called Brightwell Wiring. The name says it all, my electrical contracting business provides "Brightwell Craftsman Work" I'm open to any colors that pop and customers to say Wow. I would love to print my cards on metal.

Contact Information for Business Card

The card needs to have as follows
Name of company: Brightwell Wiring
My Name: Marco Delvane
Phone # 916-555-0147
CL# 4873920
Email: brightwellwiring@mailtorva.com
and a slogan that represent "BRIGHTWELL"

Requirements
Must have
• The card needs to have as follows
• Name of company: Brightwell Wiring
• My Name : Marco Delvane
• Phone # 916-555-0147
• CL# 4873920
• Email: brightwellwiring@mailtorva.com
• and a slogan that represent "BRIGHTWELL"
Nice to have
• popping colors
• electrical Arcing

```html
<!DOCTYPE html>
<html lang="en">
<head>
<meta charset="utf-8">
<title>Brightwell Wiring – Business Card</title>
<link rel="stylesheet" href="https://fonts.googleapis.com/css2?family=Montserrat:wght@700&family=Open+Sans:wght@400;600;700&display=swap">
<style>
  :root {
    --page-bg: #e9ebee;
    --card-navy: #0b1421;
    --card-deep: #0e1c2e;
    --glow-blue: #1d7cc0;
    --brand-blue: #1b78c2;
    --text-white: #ffffff;
    --text-soft: #e6edf5;
  }
  html, body {
    margin: 0;
    width: 1200px;
    height: 1000px;
    overflow: hidden;
    background: var(--page-bg);
  }
  .business-card {
    position: absolute;
    left: 100px;
    top: 202px;
    width: 1000px;
    height: 596px;
    overflow: hidden;
    background: linear-gradient(180deg, var(--card-navy) 0%, var(--card-deep) 100%);
    box-shadow: 0 10px 30px rgba(0,0,0,0.25);
  }
  .arc-photo {
    position: absolute;
    left: 0;
    top: 380px;
    width: 1000px;
    height: 216px;
    background: radial-gradient(ellipse 55% 70% at 50% 60%, #3f8fcb 0%, #1d6aa6 40%, rgba(14,28,46,0) 100%);
  }
  .brand-block {
    position: absolute;
    left: 68px;
    top: 100px;
    width: 420px;
    text-align: center;
  }
  .brand-square {
    display: block;
    width: 112px;
    height: 112px;
    margin: 0 auto 20px;
    background: var(--brand-blue);
  }
  .brand-name {
    margin: 0;
    font-family: "Montserrat", sans-serif;
    font-weight: 700;
    font-size: 48px;
    line-height: 1.08;
    color: var(--brand-blue);
  }
  .brand-name span { display: block; }
  .column-divider {
    position: absolute;
    left: 500px;
    top: 112px;
    width: 2px;
    height: 180px;
    background: linear-gradient(180deg, rgba(255,255,255,0) 0%, rgba(255,255,255,0.75) 50%, rgba(255,255,255,0) 100%);
  }
  .contact-block {
    position: absolute;
    left: 545px;
    top: 114px;
    font-family: "Open Sans", sans-serif;
    color: var(--text-soft);
  }
  .person-name {
    margin: 0 0 30px;
    font-size: 31px;
    line-height: 42px;
    font-weight: 700;
    color: var(--text-white);
    letter-spacing: 0.5px;
  }
  .person-name .surname { color: var(--brand-blue); }
  .contact-list { list-style: none; margin: 0; padding: 0; font-size: 22px; }
  .contact-list li { display: flex; align-items: center; height: 38px; }
  .contact-list .licence { margin-bottom: 8px; }
  .contact-icon { width: 20px; height: 20px; margin-right: 12px; flex: none; }
  .tagline {
    position: absolute;
    left: 0;
    top: 522px;
    width: 100%;
    margin: 0;
    text-align: center;
    font-family: "Open Sans", sans-serif;
    font-weight: 600;
    font-size: 26px;
    color: var(--text-white);
  }
</style>
</head>
<body>
  <section class="business-card" aria-label="Brightwell Wiring business card">
    <div class="arc-photo" role="img" aria-label="Photo of two red cables with stripped wires meeting in a bright blue-white electrical arc"></div>

    <div class="brand-block">
      <span class="brand-square" aria-hidden="true"></span>
      <p class="brand-name"><span>BRIGHTWELL</span><span>WIRING</span></p>
    </div>

    <div class="column-divider"></div>

    <div class="contact-block">
      <h1 class="person-name">MARCO <span class="surname">DELVANE</span></h1>
      <ul class="contact-list">
        <li class="licence">CL# 4873920</li>
        <li>
          <svg class="contact-icon" viewBox="0 0 20 20" aria-hidden="true">
            <path fill="#1b78c2" d="M5.2 2.5l2.6 3.1c.4.5.3 1.1-.1 1.5L6.4 8.3c.9 2 2.6 3.8 4.7 4.8l1.2-1.3c.4-.4 1.1-.5 1.5-.1l3.1 2.6c.4.4.5 1 .1 1.5l-1.3 1.6c-.6.7-1.6 1-2.5.7C8 16.6 3.9 12.5 2.3 7.3c-.3-.9 0-1.9.7-2.5l1.6-1.3c.2-.3.4-.4.6-1z"/>
          </svg>916-555-0147
        </li>
        <li>
          <svg class="contact-icon" viewBox="0 0 20 20" aria-hidden="true">
            <rect x="1" y="4" width="18" height="12" fill="#1b78c2"/>
            <path d="M1.5 4.8L10 11l8.5-6.2" fill="none" stroke="#0b1421" stroke-width="1.4"/>
          </svg>brightwellwiring@mailtorva.com
        </li>
      </ul>
    </div>

    <p class="tagline">Brightwell Quality You Can See!</p>
  </section>
</body>
</html>
```